IT Consulting company Needs a Logo Design and Business Cards

I need a New Logo and Business Cards for an established IT Managed Services Company that specializes in flat-rate managed IT services. We provide Design and Build, Help Desk, Onsite and Remote Support Services.

Target Market(s)

Corporate Clients

Industry/Entity Type

It Company

Logo Text

Halvern Systems Collective

Requirements
Nice to have
• Tag Line= Technology at Lightning Speed

```html
<!DOCTYPE html>
<html lang="en">
<head>
<meta charset="utf-8">
<title>Halvern Systems Collective – Logo and Business Cards</title>
<link href="https://fonts.googleapis.com/css2?family=Roboto+Condensed:wght@400&family=Open+Sans:wght@400&display=swap" rel="stylesheet">
<style>
  :root{
    --green-dark:#0e8945;
    --green-light:#70c494;
    --card-grey:#e2e3e4;
    --ink:#111111;
    --page:#ffffff;
  }
  html,body{margin:0;padding:0;overflow:hidden;background:var(--page);}
  .sheet{position:relative;width:1200px;height:1200px;overflow:hidden;background:var(--page);}
  .shapes{position:absolute;left:0;top:0;width:1200px;height:1200px;}
  .section-label{position:absolute;font-family:"Open Sans",sans-serif;font-size:31px;color:var(--ink);line-height:1;margin:0;}
  .cond{font-family:"Roboto Condensed",sans-serif;font-weight:400;}
  .brand-name{position:absolute;color:var(--green-dark);white-space:nowrap;margin:0;line-height:1;}
  .message{position:absolute;color:var(--ink);font-size:29px;line-height:39px;margin:0;}
  .web-link{position:absolute;color:var(--green-dark);font-size:29px;line-height:1;white-space:nowrap;}
  .tagline{position:absolute;color:var(--green-dark);font-size:12px;line-height:1;white-space:nowrap;}
  .contact{position:absolute;color:var(--green-dark);font-size:20px;line-height:1;white-space:nowrap;}
</style>
</head>
<body>
<main class="sheet">
  <svg class="shapes" viewBox="0 0 1500 1500" aria-hidden="true">
    <!-- section arrows -->
    <g fill="none" stroke="var(--ink)" stroke-width="2.5" stroke-linejoin="miter">
      <path d="M187 130 V180 H228 V204 L255 178 L228 152 V180"/>
      <path d="M187 612 V660 H228 V684 L255 658 L228 632 V660"/>
      <path d="M187 1105 V1153 H228 V1177 L255 1151 L228 1125 V1153"/>
    </g>

    <!-- brand sheet mark placeholder -->
    <circle cx="705" cy="230" r="9" fill="var(--green-dark)"/>

    <!-- front card -->
    <rect class="card-front" x="305" y="337" width="902" height="541" fill="var(--card-grey)"/>
    <polygon fill="var(--green-light)" points="580,337 650,337 762,567 745,605 662,403 620,432"/>
    <polygon fill="var(--green-dark)" points="620,432 662,403 775,672 672,878 580,878 692,608"/>
    <circle cx="850" cy="706" r="10" fill="var(--green-dark)"/>
    <g class="globe-icon" fill="none" stroke="var(--green-dark)" stroke-width="2.5">
      <circle cx="851" cy="811" r="13"/>
      <path d="M840 804 Q851 812 862 804 M840 818 Q851 810 862 818 M845 800 L857 822"/>
    </g>

    <!-- back card -->
    <rect class="card-back" x="305" y="887" width="906" height="543" fill="var(--card-grey)"/>
    <polygon fill="var(--green-light)" points="820,887 915,887 792,1160 872,1338 822,1366 703,1093"/>
    <polygon fill="var(--green-dark)" points="722,1136 822,1366 872,1338 915,1430 818,1430 692,1205"/>
    <circle cx="396" cy="957" r="9" fill="var(--green-dark)"/>

    <!-- contact icons -->
    <g fill="var(--green-light)">
      <circle cx="395" cy="1093" r="28"/>
      <circle cx="395" cy="1176" r="28"/>
      <circle cx="395" cy="1258" r="28"/>
      <circle cx="395" cy="1347" r="28"/>
    </g>
    <g fill="var(--green-dark)">
      <path d="M379 1094 L395 1078 L411 1094 H406 V1108 H399 V1099 H391 V1108 H384 V1094 Z"/>
      <path d="M380 1164 L412 1178 L392 1182 L390 1192 L386 1180 Z"/>
      <path d="M380 1255 Q395 1240 410 1255 L410 1259 L404 1259 L403 1254 H387 L386 1259 L380 1259 Z"/>
      <rect x="383" y="1260" width="24" height="11" rx="2"/>
      <circle cx="395" cy="1347" r="15"/>
    </g>
    <circle cx="395" cy="1264" r="4" fill="var(--green-light)"/>
    <g fill="none" stroke="var(--green-light)" stroke-width="1.6">
      <path d="M381 1342 Q395 1350 409 1342 M383 1354 Q395 1346 407 1354 M390 1333 L401 1361"/>
    </g>
    <g stroke="var(--green-light)" stroke-width="3">
      <line x1="455" y1="1138" x2="515" y2="1138"/>
      <line x1="455" y1="1216" x2="515" y2="1216"/>
      <line x1="455" y1="1310" x2="515" y2="1310"/>
    </g>
  </svg>

  <p class="section-label" style="left:131px;top:56px;">LOGO</p>
  <p class="section-label" style="left:122px;top:446px;">front</p>
  <p class="section-label" style="left:122px;top:834px;">Back</p>

  <!-- brand sheet -->
  <p class="brand-name cond" style="left:575px;top:174px;font-size:24px;">Halvern Systems Collective</p>

  <!-- front card -->
  <p class="message cond" style="left:278px;top:426px;">put a picture of your<br>group activity in here<br>or the company's<br>vision and mission</p>
  <p class="brand-name cond" style="left:690px;top:553px;font-size:22px;">Halvern Systems Collective</p>
  <span class="web-link cond" style="left:700px;top:634px;">urwebsitename.com</span>

  <!-- back card -->
  <p class="brand-name cond" style="left:327px;top:757px;font-size:19px;">Halvern Systems Collective</p>
  <span class="tagline cond" style="left:327px;top:786px;">Technology at Lightning Speed</span>
  <span class="contact cond" style="left:350px;top:867px;">Street Address Here</span>
  <span class="contact cond" style="left:350px;top:929px;">urname@email.com</span>
  <span class="contact cond" style="left:353px;top:999px;">YOUR PHONE</span>
  <span class="contact cond" style="left:354px;top:1067px;">www.websitename.com</span>
  <p class="message cond" style="left:722px;top:872px;">put a picture of your<br>group activity in here<br>or the company's<br>vision and mission</p>
</main>
</body>
</html>
```